Compass of Quiet Mornings book cover design

Book cover - the book contains 52 chapters - 2 for each letter of the alphabet, so a yearlong focus on Leadership. The Intent is to communicate that leadership is common sense. It just isn’t common practice. This book allows the reader to focus on one leadership word each week for a yearlong focus on improving one’s leadership. It is full of stories relating to the 52 words that will challenge and inspire the reader.
Target Market(s)
Leaders / Emerging Leaders
Industry/Entity Type
All
Requirements
Must have
- Appeal to executives
Nice to have
- Simplicity
Should not have
- Cartoon feel

```html
<!DOCTYPE html>
<html lang="en">
<head>
<meta charset="utf-8">
<title>Compass of Quiet Mornings – Book Cover</title>
<link href="https://fonts.googleapis.com/css2?family=Anton&family=Allura&family=Josefin+Sans:wght@500&display=swap" rel="stylesheet">
<style>
  :root {
    --backdrop: #767676;
    --cover-light: #eceded;
    --cover-mid: #cfd0d2;
    --green-dark: #163a20;
    --green-mid: #3f8a52;
    --gold-dark: #3f3615;
    --gold-light: #b5a566;
    --ink: #111111;
    --author-green: #1f5a2c;
    --art-green: #1f8a4e;
    --art-deep: #0f5a32;
    --art-glow: #d8e27a;
  }
  html, body {
    margin: 0;
    padding: 0;
    width: 962px;
    height: 1200px;
    overflow: hidden;
    background: var(--backdrop);
  }
  .book-cover {
    position: absolute;
    left: 113px;
    top: 48px;
    width: 736px;
    height: 1103px;
    overflow: hidden;
    background: radial-gradient(ellipse at 50% 75%, var(--cover-light) 0%, #e2e3e4 45%, var(--cover-mid) 100%);
  }
  .book-title {
    margin: 0;
    font-weight: 400;
  }
  .title-main,
  .title-end {
    position: absolute;
    left: 0;
    width: 100%;
    margin: 0;
    text-align: center;
    font-family: "Anton", sans-serif;
    font-weight: 400;
    text-transform: uppercase;
    line-height: 1;
    -webkit-background-clip: text;
    background-clip: text;
    color: transparent;
  }
  .title-main {
    top: 56px;
    font-size: 122px;
    letter-spacing: 1px;
    background-image: linear-gradient(90deg, var(--green-dark) 20%, var(--green-mid) 55%, var(--green-dark) 85%);
  }
  .title-link {
    position: absolute;
    top: 162px;
    left: 0;
    width: 100%;
    text-align: center;
    font-family: "Allura", cursive;
    font-size: 78px;
    line-height: 1;
    color: var(--ink);
  }
  .title-end {
    top: 236px;
    font-size: 124px;
    letter-spacing: -1px;
    background-image: linear-gradient(90deg, var(--gold-dark) 25%, var(--gold-light) 80%);
  }
  .cover-art {
    position: absolute;
    left: 140px;
    top: 385px;
    width: 455px;
    height: 630px;
    border-radius: 48% 48% 14% 14% / 22% 22% 6% 6%;
    background:
      radial-gradient(circle at 52% 35%, var(--art-glow) 0%, rgba(216,226,122,0) 22%),
      linear-gradient(180deg, var(--art-green) 0%, var(--art-deep) 55%, #2a8a60 80%, rgba(200,220,210,0.2) 100%);
    filter: blur(2px);
  }
  .author-name {
    position: absolute;
    top: 1036px;
    left: 0;
    width: 100%;
    margin: 0;
    text-align: center;
    font-family: "Josefin Sans", sans-serif;
    font-weight: 500;
    font-size: 38px;
    line-height: 1;
    letter-spacing: 7px;
    color: var(--author-green);
  }
</style>
</head>
<body>
  <main class="book-cover">
    <h1 class="book-title">
      <span class="title-main">Compass</span>
      <span class="title-link">of Quiet</span>
      <span class="title-end">Mornings</span>
    </h1>
    <div class="cover-art" role="img" aria-label="Illustration of green upward arrows rising behind a group of six people in silhouette"></div>
    <p class="author-name">AUTHOR NAME</p>
  </main>
</body>
</html>
```